Mental Health care Company in Washington DC

We are a new mental health care services provider in Washington DC. Please look at these sites.
https://quarrystonewellbeingpartners.com
https://www.quietharborllc.com
https://fernvale-nb.org/
https://www.truepathnb.com
https://www.willowmeadnb.com

```html
<!DOCTYPE html>
<html lang="en">
<head>
<meta charset="UTF-8">
<title>Tallowmere Health Services — Your Partner in Mental Wellness</title>
<link href="https://fonts.googleapis.com/css2?family=Inter:wght@400;500;600;700;800&display=swap" rel="stylesheet">
<style>
:root{
  --navy:#101c38;
  --navy-card:#263350;
  --ink:#3c4557;
  --muted:#5b6475;
  --orange:#e88a36;
  --teal:#a9d6dc;
  --bg-soft:#f6f8fb;
  --white:#ffffff;
  --line:#d5dbe4;
  --map:#e3e8f0;
  --testi-link:#a9c8ff;
}
*{box-sizing:border-box;margin:0;padding:0}
html,body{width:1200px;height:3250px;overflow:hidden}
body{font-family:"Inter",sans-serif;color:var(--ink);background:var(--white)}
.wrap{width:976px;margin:0 auto}
h1,h2,h3,h4{color:var(--navy);font-family:"Inter",sans-serif}

/* nav */
.site-nav{height:53px;background:var(--white);box-shadow:0 1px 4px rgba(16,28,56,.08);position:relative;z-index:2}
.site-nav .wrap{display:flex;align-items:center;justify-content:space-between;height:53px}
.brand{display:flex;align-items:center;gap:8px;font-size:18px;font-weight:600;color:var(--navy)}
.brand-dot{width:10px;height:10px;border-radius:50%;background:var(--orange)}
.nav-links{display:flex;gap:26px;font-size:13px;font-weight:600;color:var(--navy);margin-left:90px}
.nav-links .active{border-bottom:2px solid var(--orange);padding-bottom:5px}
.btn{display:inline-block;background:var(--orange);color:var(--white);font-weight:700;border-radius:999px;text-align:center}
.btn-nav{font-size:13px;padding:9px 19px}

/* hero */
.hero{height:404px;position:relative;overflow:hidden}
.hero-photo{position:absolute;inset:0;background:linear-gradient(90deg,#f3f2f0 0%,#ece8e3 45%,#e4ddd5 70%,#efebe7 100%)}
.hero .wrap{position:relative;padding-top:72px}
.hero h1{font-size:50px;line-height:1.05;font-weight:800;letter-spacing:-.5px;width:460px}
.hero p{font-size:16px;line-height:1.4;width:460px;margin-top:22px;color:var(--ink)}
.btn-hero{font-size:15px;padding:12px 32px;margin-top:26px}

/* sections */
.section-head{text-align:center}
.section-head h2{font-size:29px;font-weight:700}
.section-head p{font-size:15px;line-height:1.5;width:560px;margin:14px auto 0}

.services{background:var(--bg-soft);height:717px;padding-top:62px}
.card-grid{display:grid;grid-template-columns:repeat(3,308px);gap:26px;margin-top:40px}
.card{background:var(--white);border-radius:8px;box-shadow:0 2px 10px rgba(16,28,56,.07)}
.service{padding:26px 25px;height:230px}
.service.short{height:206px}
.service .icon{width:28px;height:28px}
.service h3{font-size:19px;font-weight:700;margin-top:14px;line-height:1.3;letter-spacing:-.2px;white-space:nowrap}
.service h3.wrap-title{white-space:normal}
.service p{font-size:13px;line-height:1.5;margin-top:10px}

.steps{height:397px;padding-top:62px}
.step-row{display:flex;justify-content:space-between;margin-top:48px;position:relative}
.step{width:300px;text-align:center;position:relative}
.step-num{width:76px;height:76px;border-radius:50%;background:var(--teal);color:var(--white);font-size:28px;font-weight:700;display:flex;align-items:center;justify-content:center}
.step h4{font-size:17px;font-weight:700;margin-top:14px}
.step p{font-size:13px;line-height:1.5;margin-top:8px}
.step-arrow{position:absolute;top:76px;width:22px;height:12px}

.team{background:var(--bg-soft);height:515px;padding-top:62px}
.member{height:260px;text-align:center;padding-top:28px}
.avatar{width:95px;height:95px;border-radius:50%;background:var(--teal);border:3px solid var(--white);box-shadow:0 2px 6px rgba(16,28,56,.12);margin:0 auto;display:flex;align-items:center;justify-content:center;font-size:42px;font-weight:600;color:var(--navy)}
.member h3{font-size:16px;font-weight:700;margin-top:14px}
.member .role{font-size:12.5px;font-weight:600;color:var(--orange);margin-top:4px}
.member p{font-size:11.5px;line-height:1.45;width:250px;margin:10px auto 0}

.stories{background:var(--navy);height:406px;padding-top:62px}
.stories h2{color:var(--white)}
.stories .section-head p{color:#dfe5ef}
.testi-grid{display:grid;grid-template-columns:475px 475px;gap:26px;margin-top:40px}
.testi{background:var(--navy-card);border-radius:8px;height:139px;padding:26px}
.testi q{display:block;font-style:italic;font-size:13px;line-height:1.5;color:#e6ebf3;quotes:none}
.testi .who{font-size:13px;font-weight:700;color:var(--testi-link);margin-top:16px}

.contact{height:675px;padding-top:62px}
.contact-card{width:709px;height:420px;margin:42px auto 0;background:var(--bg-soft);border-radius:10px;box-shadow:0 3px 14px rgba(16,28,56,.08);padding:26px;display:grid;grid-template-columns:311px 311px;gap:35px}
.contact-card h3{font-size:19px;font-weight:700}
.field label{display:block;font-size:12px;font-weight:600;color:var(--navy);margin-top:14px}
.field .input{height:32px;border:1px solid var(--line);border-radius:5px;background:var(--white);margin-top:8px}
.field .textarea{height:110px;padding:8px 12px;font-size:12px;line-height:1.5;color:#9aa2b1}
.btn-send{display:block;width:311px;font-size:12.5px;padding:11px 0;margin-top:18px}
.info{list-style:none;margin-top:14px}
.info li{display:flex;gap:10px;font-size:12.5px;line-height:1.5;color:var(--navy);margin-bottom:10px}
.info svg{width:14px;height:14px;flex:none;margin-top:2px}
.map{height:180px;background:var(--map);border-radius:6px;display:flex;align-items:center;justify-content:center;font-size:16px;color:var(--ink);margin-top:12px}

.site-footer{background:var(--navy);height:83px}
.site-footer .wrap{display:flex;justify-content:space-between;align-items:center;height:83px}
.foot-name{font-size:12.5px;font-weight:700;color:var(--white)}
.foot-tag{font-size:11px;color:#aab3c4;margin-top:3px}
.copy{font-size:11px;color:#aab3c4}
</style>
</head>
<body>

<header class="site-nav">
  <div class="wrap">
    <div class="brand"><span class="brand-dot"></span>Tallowmere Health</div>
    <nav class="nav-links"><span class="active">Home</span><span>Services</span><span>About Us</span><span>Contact</span></nav>
    <span class="btn btn-nav">Get Help Now</span>
  </div>
</header>

<section class="hero">
  <div class="hero-photo" role="img" aria-label="Softly lit group therapy session in a bright room"></div>
  <div class="wrap">
    <h1>Your Partner in Mental Wellness</h1>
    <p>Tallowmere Health Services provides compassionate, professional, and community-focused mental health care for the residents of Washington D.C. Your journey to a healthier mind starts here.</p>
    <span class="btn btn-hero">Schedule a Consultation</span>
  </div>
</section>

<section class="services">
  <div class="wrap">
    <div class="section-head">
      <h2>Our Holistic Approach to Care</h2>
      <p>We treat the whole person, not just the symptoms. Our services are designed to support your mental, emotional, and social well-being.</p>
    </div>
    <div class="card-grid">
      <div class="card service">
        <svg class="icon" viewBox="0 0 28 28"><circle cx="14" cy="9" r="6" fill="#5a7aa0"/><path d="M3 27c0-7 5-10 11-10s11 3 11 10z" fill="#5a7aa0"/></svg>
        <h3>Individual Therapy</h3>
        <p>A confidential space to explore your thoughts and feelings with a dedicated professional, developing strategies for growth and healing.</p>
      </div>
      <div class="card service">
        <svg class="icon" viewBox="0 0 28 28"><rect x="1" y="1" width="26" height="26" rx="5" fill="#7b9cc4"/><circle cx="10" cy="11" r="3.5" fill="#fff"/><circle cx="18" cy="11" r="3.5" fill="#fff"/><path d="M4 23c0-4 3-6 6-6s6 2 6 6zM12 23c0-4 3-6 6-6s6 2 6 6z" fill="#fff"/></svg>
        <h3 class="wrap-title">Family &amp; Couples<br>Counseling</h3>
        <p>Improve communication and resolve conflicts to build stronger, healthier relationships with the people who matter most.</p>
      </div>
      <div class="card service">
        <svg class="icon" viewBox="0 0 28 28"><ellipse cx="14" cy="14" rx="13" ry="10" fill="#e07a96"/><path d="M14 5v18M7 10c3 1 3 4 0 5M21 10c-3 1-3 4 0 5" stroke="#b8506c" stroke-width="1.5" fill="none"/></svg>
        <h3>Psychiatry &amp; Medication</h3>
        <p>Comprehensive psychiatric evaluations and medication management as part of a holistic treatment plan.</p>
      </div>
      <div class="card service short">
        <svg class="icon" viewBox="0 0 28 28"><path d="M2 12l7-5 5 3 5-3 7 5-9 9z" fill="#f1b437"/></svg>
        <h3>Community Support</h3>
        <p>Connecting you with resources and support systems within the D.C. community to foster a sense of belonging and stability.</p>
      </div>
      <div class="card service short">
        <svg class="icon" viewBox="0 0 28 28"><path d="M4 20c6 0 10-4 12-12l8-4-4 8c-2 8-8 12-16 8z" fill="#c9ced6"/></svg>
        <h3>Trauma-Informed Care</h3>
        <p>Specialized care that recognizes and responds to the impact of trauma, creating a safe environment for healing.</p>
      </div>
      <div class="card service short">
        <svg class="icon" viewBox="0 0 28 28"><rect x="4" y="3" width="20" height="24" rx="2" fill="#b88954"/><rect x="7" y="6" width="14" height="18" fill="#fff"/><rect x="10" y="1" width="8" height="5" rx="1" fill="#8a8f99"/></svg>
        <h3>Assessments &amp; Evaluations</h3>
        <p>Thorough and compassionate assessments to understand your unique needs and create the right plan for you.</p>
      </div>
    </div>
  </div>
</section>

<section class="steps">
  <div class="wrap">
    <div class="section-head">
      <h2>Your Path to Wellness is Clear</h2>
      <p style="width:600px">We make getting started simple and stress-free. Here's what you can expect.</p>
    </div>
    <div class="step-row">
      <div class="step"><div class="step-num">1</div><h4>Initial Consultation</h4><p>Reach out for a confidential chat to discuss your needs and see how we can help.</p></div>
      <svg class="step-arrow" style="left:291px" viewBox="0 0 22 12"><path d="M0 6h19M14 1l6 5-6 5" stroke="#a9d6dc" stroke-width="2" fill="none"/></svg>
      <div class="step"><div class="step-num">2</div><h4>Personalized Plan</h4><p>We'll match you with the right therapist and create a care plan tailored specifically to you.</p></div>
      <svg class="step-arrow" style="left:637px" viewBox="0 0 22 12"><path d="M0 6h19M14 1l6 5-6 5" stroke="#a9d6dc" stroke-width="2" fill="none"/></svg>
      <div class="step"><div class="step-num">3</div><h4>Ongoing Support</h4><p>Begin your therapy journey with consistent, compassionate support every step of the way.</p></div>
    </div>
  </div>
</section>

<section class="team">
  <div class="wrap">
    <div class="section-head">
      <h2>Our Dedicated Team</h2>
      <p>We are licensed professionals committed to the D.C. community. Building a personal, trusting relationship with you is our highest priority.</p>
    </div>
    <div class="card-grid">
      <div class="card member"><div class="avatar">ML</div><h3>Dr. Mara Linwood</h3><div class="role">Lead Psychologist, PhD</div><p>With over 15 years of experience, Dr. Linwood specializes in cognitive-behavioral therapy and trauma-informed care.</p></div>
      <div class="card member"><div class="avatar">TA</div><h3>Theo Alvarez</h3><div class="role">Licensed Professional Counselor</div><p>Theo focuses on family systems and couples counseling, helping clients build stronger communication patterns.</p></div>
      <div class="card member"><div class="avatar">RO</div><h3>Dr. Rina Okafor</h3><div class="role">Psychiatrist, MD</div><p>Dr. Okafor provides expert psychiatric evaluations and medication management with a patient-centered approach.</p></div>
    </div>
  </div>
</section>

<section class="stories">
  <div class="wrap">
    <div class="section-head">
      <h2>Stories of Hope</h2>
      <p>You are not alone. Read what others in our community have to say about their journey with us.</p>
    </div>
    <div class="testi-grid">
      <div class="testi"><q>"Finding Tallowmere Health was a turning point for me. My therapist created a space where I felt safe and truly heard for the first time. I've learned so much about myself."</q><div class="who">- A.W., Washington D.C.</div></div>
      <div class="testi"><q>"The team at Tallowmere Health helped our family navigate a really difficult time. The counseling we received gave us the tools to communicate and support each other in a healthier way."</q><div class="who">- The R. Family, Washington D.C.</div></div>
    </div>
  </div>
</section>

<section class="contact">
  <div class="wrap">
    <div class="section-head">
      <h2>Take the First Step</h2>
      <p>Reaching out is a sign of strength. Contact us today to schedule your confidential consultation. Our team is ready to help.</p>
    </div>
    <div class="contact-card">
      <div>
        <h3>Send Us a Message</h3>
        <div class="field"><label>Full Name</label><div class="input"></div></div>
        <div class="field"><label>Email Address</label><div class="input"></div></div>
        <div class="field"><label>Message</label><div class="input textarea">Briefly tell us what you're looking for. (Please do not include sensitive health information.)</div></div>
        <span class="btn btn-send">Send Secure Message</span>
      </div>
      <div>
        <h3>Contact Information</h3>
        <ul class="info">
          <li><svg viewBox="0 0 14 14"><path d="M7 1a4 4 0 0 1 4 4c0 3-4 8-4 8S3 8 3 5a4 4 0 0 1 4-4z" fill="#d9434a"/><circle cx="7" cy="5" r="1.4" fill="#fff"/></svg><span>48 Harborview Lane<br>Washington, D.C. 20005</span></li>
          <li><svg viewBox="0 0 14 14"><path d="M3 1l3 3-1.5 2a8 8 0 0 0 3.5 3.5L10 8l3 3-2 2C6 13 1 8 1 3z" fill="#3c4557"/></svg><span>(202) 555-0147</span></li>
          <li><svg viewBox="0 0 14 14"><rect x="1" y="3" width="12" height="8" rx="1" fill="#c9ced6"/><path d="M1 3l6 5 6-5" stroke="#fff" fill="none"/></svg><span>hello@tallowmerehealth.com</span></li>
        </ul>
        <div class="map" role="img" aria-label="Map of Washington D.C.">Map of Washington D.C.</div>
      </div>
    </div>
  </div>
</section>

<footer class="site-footer">
  <div class="wrap">
    <div><div class="foot-name">Tallowmere Health Services</div><div class="foot-tag">Your Partner in Mental Wellness</div></div>
    <div class="copy">© 2025 Tallowmere Health Services. All Rights Reserved.</div>
  </div>
</footer>

</body>
</html>
```